Facebook Design Project

"Sun-Crest Coffee Kiosks" should be the page name.

Sun-Crest provides coffee carts, kiosks, and drive thrus to the Triangle (Raleigh/Durham, NC) serving the health conscious, on the go! We can set up in business offices/towers, campuses, hospitals, fitness centers or other high foot traffic locations. Sun-Crest offers certified, fair trade Nicaraguan coffee / espresso drinks, 100% fruit smoothies, protein shakes & healthy bites, to go!

Company will promote: health/wellness, protecting the environment & giving back to the community and to Nicaragua (10% of profits will help support Bright Path Outreach Nicaragua www.brightpathout.org )
Updates

I have updated my design needs. Thanks, Danielle

Target Market(s)

18-54, affluent coffee/espresso drinkers.

Industry/Entity Type

Environment

Requirements
Must have
• -Include my website (which is under construction) www.Sun-Crest.com
-Contact info: Email: danielle@sun-crest.com Phone number: 919-555-0147
-Twitter: @suncrestcoffee
-"Crest Tip of the day" This will be a daily wellness tip/post pertaining to nutrition, exercise and or mental well-being.

List:

"Organic Coffee & Espresso Drinks"
"100% Fruit Smoothies & Protein Shakes"
"Healthy Bites, To-Go"
"Fundraisers"
"Coffee Catering"

Tagline: "Break the fast!"
Nice to have
• I have attached my logo and business card (front and back). I would like to stay with same colors (dark brown, light brown and lime green)

-Put Sun-Crest's logo on a "to go" coffee cup but I would like it to look better than just the brown logo on a white cup. Maybe add the lime green color in some how. I have source files for the logo if you need to make changes.
Should not have
• Don't use cursive or weird fonts.

```html
<!DOCTYPE html>
<html lang="en">
<head>
<meta charset="utf-8">
<title>Sun-Crest Coffee Kiosks — Cover</title>
<link rel="stylesheet" href="https://fonts.googleapis.com/css2?family=Oswald:wght@300;400&family=Days+One&family=Dosis:wght@500&family=Pathway+Gothic+One&display=swap">
<style>
  :root {
    --backdrop: #2a170d;
    --lime: #a8cf3e;
    --lime-text: #b4d94a;
    --roast: #7f3a2a;
    --espresso: #3b1f12;
    --white: #ffffff;
    --ink: #1d1d1d;
  }
  * { margin: 0; padding: 0; box-sizing: border-box; }
  html, body {
    width: 1200px; height: 1000px; overflow: hidden;
    background: var(--backdrop);
  }
  .canvas { position: relative; width: 1200px; height: 1000px; }

  .cover {
    position: absolute; left: 105px; top: 318px;
    width: 850px; height: 312px;
    background: var(--roast);
    overflow: hidden;
  }
  .cover__band {
    position: absolute; left: 0; top: 0; width: 100%; height: 50px;
    background: var(--lime);
  }
  .brand {
    position: absolute; left: 0; top: 62px; width: 100%;
    text-align: center; color: var(--lime-text);
  }
  .brand__mark {
    display: block; margin: 0 auto 6px;
    width: 56px; height: 56px; border-radius: 50%;
    background: var(--espresso);
  }
  .brand__name {
    font-family: "Oswald", sans-serif; font-weight: 400;
    font-size: 72px; line-height: 1; letter-spacing: 1px;
  }
  .brand__sub {
    margin-top: 6px; margin-left: 30px;
    font-family: "Days One", sans-serif; font-size: 17px; letter-spacing: 1px;
  }
  .tagline {
    position: absolute; left: 0; top: 240px; width: 890px;
    text-align: center; color: var(--lime-text);
    font-family: "Dosis", sans-serif; font-weight: 500;
    font-size: 23px; letter-spacing: 4px;
  }

  .contact {
    position: absolute; left: 680px; top: 216px;
    list-style: none; color: var(--lime-text);
    font-family: "Pathway Gothic One", sans-serif; font-size: 16px; line-height: 18px;
  }
  .contact li { display: flex; align-items: center; gap: 6px; }
  .contact svg { width: 15px; height: 15px; flex: none; }

  .profile {
    position: absolute; left: 129px; top: 512px;
    width: 168px; height: 168px;
    background: var(--white); padding: 4px;
    border: 1px solid #c9c9c9;
  }
  .profile__inner {
    position: relative; width: 100%; height: 100%;
    background: var(--lime);
  }
  .profile__mark {
    position: absolute; left: 48px; top: 10px;
    width: 60px; height: 60px; border-radius: 50%;
    background: var(--roast);
  }
  .profile__cup {
    position: absolute; left: 28px; top: 86px; width: 102px; height: 62px;
    border-radius: 50% / 40%;
    background: radial-gradient(ellipse at 55% 40%, #f2f2f2 0%, #d0d0d0 55%, #6b3f22 100%);
  }

  .page-name {
    position: absolute; left: 308px; top: 642px;
    font-family: "Pathway Gothic One", sans-serif; font-size: 30px;
    letter-spacing: 3px; color: var(--white);
  }
</style>
</head>
<body>
<div class="canvas">
  <section class="cover">
    <div class="cover__band"></div>
    <div class="brand">
      <span class="brand__mark"></span>
      <div class="brand__name">Sun-Crest</div>
      <div class="brand__sub">ORGANIC COFFEE</div>
    </div>
    <p class="tagline">“BREAK THE FAST”</p>
    <ul class="contact">
      <li>
        <svg viewBox="0 0 16 16"><rect x="1" y="3" width="14" height="10" fill="none" stroke="currentColor" stroke-width="1.6"/><path d="M1 3l7 6 7-6" fill="none" stroke="currentColor" stroke-width="1.6"/></svg>
        danielle@sun-crest.com
      </li>
      <li>
        <svg viewBox="0 0 16 16"><circle cx="8" cy="8" r="7.5" fill="currentColor"/><path d="M5 4l2 2-1 1.2c.6 1.3 1.6 2.3 2.8 2.8L10 9l2 2-1.4 1.5C7.5 12 4 8.5 3.5 5.4z" fill="var(--roast)"/></svg>
        919-555-0147
      </li>
      <li>
        <svg viewBox="0 0 16 16"><circle cx="8" cy="8" r="7" fill="currentColor"/></svg>
        @suncrestcoffee
      </li>
    </ul>
  </section>

  <div class="profile">
    <div class="profile__inner">
      <span class="profile__mark"></span>
      <div class="profile__cup" role="img" aria-label="Cup of coffee on a saucer with scattered coffee beans"></div>
    </div>
  </div>

  <h1 class="page-name">Sun-Crest Coffee Kiosks</h1>
</div>
</body>
</html>
```